Physical Large Banner For Corporate Event

Hi, we would like a large banner designed for a corporate event using adobe illustrator/pdf. The size of the banner must be 2000 (h)x800 (w) mm to fit with the printing requirements (please visit https://www.bannora.com/products/48/banner-stands and see the guidelines for size for a standard banner)

Our organisation holds events for students to find out more on top careers such as Investment Banking & Law. The banner design can be fairly simple but bold using the same themes and colours on our website www.brightpathlearning.co.uk. We can provide imagery of our logo for use/other pictures requested such as those for students/cityscapes etc.

The only text on the banner should be our web address at the bottom (www.brightpathlearning.co.uk) and a line that says "A Head Start in the City, We bring the internship to you..." like in our website homepage.

Target Market(s)

Students & Graduate Recruiters

Industry/Entity Type

Education

Requirements
Must have
• Website address
• Cool imagery
Should not have
• Too much clutter, clean and simple pleaseE

```html
<!DOCTYPE html>
<html lang="en">
<head>
<meta charset="utf-8">
<title>BrightPath – Roll-up Banner</title>
<link href="https://fonts.googleapis.com/css2?family=Open+Sans:wght@300;400;600;700;800&display=swap" rel="stylesheet">
<style>
  :root {
    --stage: #444444;
    --paper: #ffffff;
    --ink: #111111;
    --grey: #8e8e8e;
    --grey-dark: #555555;
    --grey-light: #a6a6a6;
    --red: #8a1218;
    --rule: #6f6f6f;
  }
  html, body {
    margin: 0;
    padding: 0;
    width: 1200px;
    height: 1000px;
    overflow: hidden;
    background: var(--stage);
    font-family: "Open Sans", Arial, sans-serif;
  }
  .banner {
    position: absolute;
    left: 412px;
    top: 30px;
    width: 376px;
    height: 940px;
    background: var(--paper);
    box-shadow: 6px 8px 14px rgba(0,0,0,0.45);
  }
  .brand-name {
    position: absolute;
    top: 178px;
    left: 0;
    width: 100%;
    text-align: center;
    font-size: 52px;
    font-weight: 400;
    color: var(--grey-dark);
    letter-spacing: 1px;
    line-height: 1;
    margin: 0;
  }
  .brand-rule {
    position: absolute;
    top: 251px;
    left: 23px;
    width: 315px;
    height: 1px;
    background: var(--rule);
  }
  .headline {
    margin: 0;
    font-weight: normal;
  }
  .headline span {
    position: absolute;
    left: 32px;
    line-height: 1;
    white-space: nowrap;
  }
  .line-head-start { top: 328px; font-size: 43px; font-weight: 700; color: var(--grey-light); }
  .line-city { top: 383px; font-size: 36px; font-weight: 400; color: var(--ink); letter-spacing: 5px; }
  .line-we-bring { top: 425px; font-size: 68px; font-weight: 300; color: var(--grey); letter-spacing: -1px; }
  .line-internship { top: 507px; font-size: 39px; font-weight: 700; color: var(--ink); letter-spacing: -0.5px; }
  .line-to-you { top: 552px; left: 40px !important; font-size: 66px; font-weight: 800; color: var(--red); letter-spacing: -1px; }

  .contact-rule {
    position: absolute;
    left: 0;
    width: 80px;
    height: 2px;
    background: linear-gradient(to right, rgba(110,110,110,0.2), #6a6a6a);
  }
  .contact-item {
    position: absolute;
    left: 100px;
    display: flex;
    align-items: flex-start;
    gap: 8px;
    font-size: 11px;
    color: var(--grey-dark);
    line-height: 13px;
  }
  .contact-item svg { flex: none; }
  .contact-email { top: 698px; }
  .contact-phone { top: 734px; }
  .contact-address { top: 786px; }
  .address-lines { padding-top: 0; margin: 0; font-style: normal; }

  .web {
    position: absolute;
    left: 18px;
    top: 886px;
    display: flex;
    align-items: center;
    gap: 12px;
  }
  .web-dot {
    width: 32px;
    height: 32px;
    border-radius: 50%;
    background: var(--red);
  }
  .web-address {
    font-size: 18px;
    font-weight: 700;
    color: var(--grey-dark);
  }
</style>
</head>
<body>
  <main class="banner">
    <p class="brand-name">BrightPath</p>
    <div class="brand-rule"></div>

    <h1 class="headline">
      <span class="line-head-start">A Head Start</span>
      <span class="line-city">in the City,</span>
      <span class="line-we-bring">We bring</span>
      <span class="line-internship">the internship</span>
      <span class="line-to-you">to you...</span>
    </h1>

    <div class="contact-rule" style="top:706px"></div>
    <div class="contact-rule" style="top:744px"></div>
    <div class="contact-rule" style="top:795px"></div>

    <div class="contact-item contact-email">
      <svg width="22" height="15" viewBox="0 0 22 15" aria-hidden="true">
        <rect x="0.75" y="0.75" width="20.5" height="13.5" fill="none" stroke="#666" stroke-width="1.5"/>
        <polyline points="1,1 11,9 21,1" fill="none" stroke="#666" stroke-width="1.5"/>
        <polyline points="1,14 8,7 M21,14 14,7" fill="none" stroke="#666" stroke-width="1.2"/>
      </svg>
      <span>info@brightpathlearning.co.uk</span>
    </div>

    <div class="contact-item contact-phone">
      <svg width="14" height="22" viewBox="0 0 14 22" aria-hidden="true">
        <rect x="1" y="1" width="12" height="20" rx="2" fill="none" stroke="#666" stroke-width="1.5"/>
        <line x1="1" y1="17" x2="13" y2="17" stroke="#666" stroke-width="1.2"/>
      </svg>
      <span style="padding-left:8px;padding-top:4px">0800 318 5526</span>
    </div>

    <div class="contact-item contact-address">
      <svg width="14" height="22" viewBox="0 0 14 22" aria-hidden="true">
        <path d="M7 21 C7 21 1 11 1 7 A6 6 0 0 1 13 7 C13 11 7 21 7 21 Z" fill="#7a7a7a"/>
        <circle cx="7" cy="7" r="2.3" fill="#fff"/>
      </svg>
      <address class="address-lines" style="margin-left:8px;margin-top:-12px">
        BrightPath<br>
        BrightPath Learning Ltd<br>
        12 Harbour Court<br>
        48 Elmwood Street<br>
        London<br>
        N1 4BX
      </address>
    </div>

    <div class="web">
      <div class="web-dot"></div>
      <span class="web-address">www.brightpathlearning.co.uk</span>
    </div>
  </main>
</body>
</html>
```